Design a refer a friend Flyer (French & English)
Flyer Title:
Main Title: "Refer a Friend & Receive a Free Electric Toothbrush!"
Bold and clear, centered at the top.
Use a clean and modern font.
Color: White text on a vivid green background for maximum contrast and readability.
Visual Focus:
Toothbrush Image: Place a high-quality image of the Dentiva Glide 300 Electric Toothbrush in the center of the flyer.
Include a small price tag with “Value of $50” near the toothbrush to highlight the reward.
Simple Message:
Text: "Refer a friend to Centre Dentaire Val-Fleuri. When they book and attend their appointment, you get a free electric toothbrush, and they receive a special gift!"
Straightforward and easy to understand.
Placed below the image of the toothbrush.
Referral Process:
3 Easy Steps:
Refer a Friend
They Book and Come to Their Appointment
Receive Your Free Electric Toothbrush
Use simple, minimal icons to visually represent each step.
Keep the steps aligned horizontally or vertically for clarity.
Call to Action:
Text: "Start Referring Today!"
Place it in a button-like design in the vivid green color with bold, white text to make it stand out.
Contact Information:
Details:
Logo of Centre Dentaire Val-Fleuri.
Address: "48 Rue Lambert Ouest, Suite 210".
Phone Number and Website: Positioned at the bottom for easy reference.
Color Scheme:
Use a vivid green background for the entire flyer, with white accents for text and icons to maintain a fresh, clean look.
Minimal clutter, focusing on clarity and the key elements: the toothbrush, the call to action, and contact information.
Clinic : www.cdvalfleuri-example.com
Attached is the brandbook, logo and inspo I made with AI.
French text will be provided.
Thank you,
Idris

```html
<!DOCTYPE html>
<html lang="en">
<head>
<meta charset="utf-8">
<title>Refer a Friend Flyer – Clinique Dentaire Val-Fleuri</title>
<link rel="stylesheet" href="https://fonts.googleapis.com/css2?family=Outfit:wght@300;400;500;600;700;800&family=Oswald:wght@600&display=swap">
<style>
  :root {
    --green: #00ad50;
    --green-light: #3fc46c;
    --green-dark: #00963f;
    --white: #ffffff;
    --paper: #f3f4f3;
    --stage: #dfe5e4;
  }
  * { box-sizing: border-box; margin: 0; padding: 0; }
  html, body { width: 1200px; height: 1117px; overflow: hidden; }
  body {
    background: var(--stage);
    font-family: "Outfit", sans-serif;
    color: var(--white);
    position: relative;
  }
  .flyer {
    position: absolute;
    left: 226px; top: 28px;
    width: 748px; height: 1060px;
    background: linear-gradient(180deg, var(--green) 0%, var(--green) 45%, var(--green-light) 100%);
    overflow: hidden;
  }
  .bottom-wave {
    position: absolute; left: 0; top: 0; width: 748px; height: 1060px;
  }
  .headline {
    position: absolute; left: 72px; top: 44px;
    font-size: 45px; line-height: 46.5px; font-weight: 800;
    letter-spacing: 0.2px; text-transform: uppercase;
  }
  .brand {
    position: absolute; left: 366px; top: 50px;
    display: flex; align-items: center; gap: 10px;
    font-size: 23px; font-weight: 600; line-height: 25px;
  }
  .brand-dot {
    width: 26px; height: 26px; border-radius: 50%;
    background: var(--white); flex: none;
  }
  .intro {
    position: absolute; left: 72px; top: 290px; width: 440px;
    font-size: 16.8px; font-weight: 300; line-height: 21.3px;
  }
  .tagline {
    position: absolute; left: 72px; top: 403px;
    font-size: 19px; font-weight: 700; line-height: 25px;
  }
  .steps-card {
    position: absolute; left: 36px; top: 505px;
    width: 432px; height: 426px;
    border: 3px solid var(--white); border-radius: 26px;
  }
  .steps-card-inner {
    position: absolute; left: 39px; top: 512px;
    width: 426px; height: 417px;
    background: var(--green); border-radius: 20px;
  }
  .steps-label {
    position: absolute; left: 72px; top: 538px;
    font-size: 24px; font-weight: 600;
  }
  .steps-band {
    position: absolute; left: 0; top: 576px;
    width: 423px; height: 59px;
    background: var(--green-dark); border-radius: 0 30px 30px 0;
  }
  .steps-title {
    position: absolute; left: 72px; top: 578px;
    font-size: 39px; font-weight: 700; line-height: 54px;
  }
  .step {
    position: absolute; left: 74px;
    display: flex; align-items: center; gap: 16px;
    font-size: 22px; font-weight: 600; line-height: 25px;
  }
  .step-icon {
    width: 72px; height: 72px; border-radius: 50%;
    border: 3px solid var(--white);
    display: flex; align-items: center; justify-content: center; flex: none;
  }
  .step-icon svg { width: 40px; height: 40px; }
  .step--one { top: 654px; }
  .step--two { top: 738px; }
  .step--three { top: 823px; }
  .value-sticker {
    position: absolute; left: 341px; top: 395px;
    width: 152px; height: 152px; border-radius: 50%;
    background: var(--paper);
    box-shadow: 0 6px 14px rgba(0,0,0,0.18);
    color: var(--green);
    text-align: center;
  }
  .value-sticker .value-label {
    position: absolute; left: 22px; top: 38px; width: 70px;
    font-size: 15px; font-weight: 800; line-height: 14px;
  }
  .value-sticker .value-amount {
    position: absolute; left: 20px; top: 64px;
    font-size: 52px; font-weight: 800; line-height: 56px;
  }
  .product-visual {
    position: absolute; left: 533px; top: 103px;
    width: 124px; height: 830px;
    border-radius: 60px 60px 40px 40px;
    background: linear-gradient(90deg, #e7ecee 0%, #ffffff 45%, #dfe4e8 100%);
    box-shadow: 0 10px 18px rgba(0,0,0,0.12);
  }
  .contact {
    position: absolute; left: 58px; top: 966px;
    display: flex; align-items: center;
    color: var(--green);
  }
  .contact-phone {
    display: flex; align-items: center; gap: 10px;
    font-family: "Oswald", sans-serif; font-size: 44px; font-weight: 600;
    letter-spacing: -0.5px; line-height: 60px;
  }
  .contact-phone svg { width: 34px; height: 34px; }
  .contact-divider {
    width: 2px; height: 54px; background: var(--green);
    margin: 0 22px 0 22px;
  }
  .contact-details { font-size: 18.5px; font-weight: 600; line-height: 28px; }
  .contact-line { display: flex; align-items: center; gap: 8px; }
  .contact-line svg { width: 16px; height: 16px; }
</style>
</head>
<body>
  <main class="flyer">
    <svg class="bottom-wave" viewBox="0 0 748 1060" aria-hidden="true">
      <path d="M0 958 Q180 930 340 905 Q560 860 748 910 L748 1060 L0 1060 Z" fill="var(--paper)"/>
    </svg>

    <h1 class="headline">Refer a<br>friend<br>&amp; receive<br>a free electric<br>toothbrush!</h1>

    <div class="brand">
      <span>Clinique Dentaire<br>Val-Fleuri</span>
      <span class="brand-dot"></span>
    </div>

    <p class="intro">Refer a friend to Centre Dentaire Val-Fleuri. When they book and attend their appointment, you get a free electric toothbrush, and they receive a special gift!</p>

    <p class="tagline">Straightforward and<br>easy to understand.</p>

    <div class="steps-card"></div>
    <div class="steps-card-inner"></div>
    <p class="steps-label">Referral Process</p>
    <div class="steps-band"></div>
    <h2 class="steps-title">3 Easy Steps</h2>

    <div class="step step--one">
      <span class="step-icon">
        <svg viewBox="0 0 40 40" fill="var(--white)" aria-hidden="true">
          <circle cx="17" cy="12" r="7"/>
          <path d="M4 34 Q4 21 17 21 Q24 21 27 25 L27 34 Z"/>
          <circle cx="30" cy="28" r="7" fill="var(--white)"/>
          <path d="M30 24 V32 M26 28 H34" stroke="var(--green)" stroke-width="2.4"/>
        </svg>
      </span>
      <span>Refer a Friend</span>
    </div>

    <div class="step step--two">
      <span class="step-icon">
        <svg viewBox="0 0 40 40" fill="none" stroke="var(--white)" stroke-width="2.6" aria-hidden="true">
          <rect x="5" y="8" width="28" height="24" rx="3"/>
          <path d="M5 15 H33 M12 5 V11 M26 5 V11"/>
          <path d="M10 20 H14 M18 20 H22 M10 26 H14 M18 26 H22" stroke-width="3"/>
        </svg>
      </span>
      <span>They Book and Come<br>to Their Appointment</span>
    </div>

    <div class="step step--three">
      <span class="step-icon">
        <svg viewBox="0 0 40 40" fill="none" stroke="var(--white)" stroke-width="2.6" aria-hidden="true">
          <rect x="16" y="14" width="8" height="20" rx="3" fill="var(--white)"/>
          <path d="M20 14 V5"/>
          <path d="M10 19 Q7 24 10 29 M30 19 Q33 24 30 29"/>
        </svg>
      </span>
      <span>Receive Your Free<br>Electric Toothbrush</span>
    </div>

    <div class="value-sticker">
      <span class="value-label">VALUE<br>OF</span>
      <span class="value-amount">$50</span>
    </div>

    <div class="product-visual" role="img" aria-label="Photo of the white Dentiva Glide 300 electric toothbrush standing upright"></div>

    <footer class="contact">
      <div class="contact-phone">
        <svg viewBox="0 0 34 34" aria-hidden="true">
          <circle cx="17" cy="17" r="17" fill="var(--green)"/>
          <path d="M11 9 L14 9 L15.5 13 L13.5 14.5 Q15.5 19 19.5 20.5 L21 18.5 L25 20 L25 23 Q24 25.5 21 25 Q10 22.5 9 12 Q9 9.5 11 9 Z" fill="var(--white)"/>
        </svg>
        <span>514-555-0182</span>
      </div>
      <span class="contact-divider"></span>
      <div class="contact-details">
        <div class="contact-line">
          <svg viewBox="0 0 16 16" aria-hidden="true"><path d="M8 1 Q13 1 13 6 Q13 10 8 15 Q3 10 3 6 Q3 1 8 1 Z" fill="var(--green)"/><circle cx="8" cy="6" r="2" fill="var(--paper)"/></svg>
          <span>48 Rue Lambert Ouest, Suite 210</span>
        </div>
        <div class="contact-line">
          <svg viewBox="0 0 16 16" fill="none" stroke="var(--green)" stroke-width="1.6" aria-hidden="true"><circle cx="8" cy="8" r="6.5"/><path d="M1.5 8 H14.5 M8 1.5 Q4.5 8 8 14.5 Q11.5 8 8 1.5"/></svg>
          <span>cdvalfleuri-example.com</span>
        </div>
      </div>
    </footer>
  </main>
</body>
</html>
```